Postcard promoting HIPAA services, including training, risk assessments, policies, etc.

I am planning a campaign to medical practices advertising HIPAA services. The primary message to convey is that HIPAA random audits are beginning in early 2016, is your practice ready. I need a full-color front design, 4.25 x 6. The design should convey some sense of urgency, and should be dramatic enough to catch the attention of a busy medical practice.

Target Market(s)

Medical, dental, chiropractic, and counseling practices

Industry/Entity Type

Doctor

Font styles to use
Sans Serif

Requirements
Must have
• Sense of urgency, specific mention of upcoming HIPAA audits, feeling that smaller practices are not exempt.

```html
<!DOCTYPE html>
<html lang="en">
<head>
<meta charset="utf-8">
<title>HIPAA Random Audits Postcard</title>
<link rel="stylesheet" href="https://fonts.googleapis.com/css2?family=Oswald:wght@400;700&display=swap">
<style>
  :root {
    --burnt-orange: #d4572e;
    --paper: #ffffff;
    --ink-grey: #6d6e70;
    --text-white: #ffffff;
  }
  * { margin: 0; padding: 0; box-sizing: border-box; }
  html, body {
    width: 850px;
    height: 1200px;
    overflow: hidden;
    background: var(--paper);
  }
  .postcard {
    position: relative;
    width: 850px;
    height: 1200px;
    background: var(--burnt-orange);
    font-family: "Oswald", "Arial Narrow", sans-serif;
    overflow: hidden;
  }
  .dot-field {
    position: absolute;
    left: 58px;
    top: 58px;
    width: 734px;
    height: 968px;
    background: var(--burnt-orange);
    border: 4px solid var(--paper);
  }
  .headline {
    position: absolute;
    left: 0;
    top: 0;
    width: 850px;
    text-align: center;
    color: var(--text-white);
    font-weight: 700;
    text-transform: uppercase;
  }
  .headline span {
    position: absolute;
    left: 0;
    width: 850px;
    display: block;
    line-height: 1;
  }
  .line-hipaa  { top: 262px; font-size: 196px; letter-spacing: 2px; }
  .line-random { top: 456px; font-size: 78px; letter-spacing: 1px; }
  .line-begins { top: 532px; font-size: 78px; letter-spacing: 0px; }
  .line-year   { top: 600px; font-size: 210px; letter-spacing: 4px; }
  .line-and    { top: 798px; font-size: 70px; letter-spacing: 0px; }
  .line-ready  { top: 866px; font-size: 70px; letter-spacing: 1px; }
  .footer-band {
    position: absolute;
    left: 0;
    top: 1042px;
    width: 850px;
    height: 158px;
    background: var(--paper);
  }
  .brand {
    position: absolute;
    left: 60px;
    top: 1078px;
    display: flex;
    align-items: center;
    gap: 12px;
  }
  .brand-mark {
    width: 30px;
    height: 30px;
    background: var(--burnt-orange);
  }
  .brand-name {
    font-size: 40px;
    font-weight: 400;
    color: var(--ink-grey);
    line-height: 1;
  }
  .brand-tagline {
    position: absolute;
    left: 60px;
    top: 1132px;
    font-size: 14px;
    font-weight: 400;
    color: var(--ink-grey);
    letter-spacing: 0.5px;
  }
</style>
</head>
<body>
  <div class="postcard">
    <div class="dot-field" role="img" aria-label="Field of small white polka dots on orange"></div>
    <h1 class="headline">
      <span class="line-hipaa">HIPAA</span>
      <span class="line-random">Random Audits</span>
      <span class="line-begins">Begins in Early</span>
      <span class="line-year">2016</span>
      <span class="line-and">And Practices Need</span>
      <span class="line-ready">To Be Ready</span>
    </h1>
    <div class="footer-band"></div>
    <div class="brand">
      <div class="brand-mark"></div>
      <div class="brand-name">CareVault</div>
    </div>
    <div class="brand-tagline">Your Healthcare IT Partner</div>
  </div>
</body>
</html>
```